Business Card for a Floral & Decorating Business

I would like to take my current logo and create a better business card. I am looking for elegance as I am a florist and event decorator. My logo has multiple colour options. I like colours like green, purple, pink and orange, I think I would like a white card, open to black back ground. I want it to feel elegant and romantic. I like metallic lettering that maybe is indented in the paper, I also like glossy paper. I have a full logo already as well as a badge. I have attached both in multiple colours.m
Updates

Need extra days to review

Target Market(s)

Weddings, special events, floral customers

Industry/Entity Type

Floral and decorating

Contact Information for Business Card

Phone number, email, instagram, facebook, title, name, logo

Font styles to use
Script

Requirements
Nice to have
• Elegant

```html
<!DOCTYPE html>
<html lang="en">
<head>
<meta charset="utf-8">
<title>Marren Ashby — Business Card</title>
<link rel="stylesheet" href="https://fonts.googleapis.com/css2?family=Cormorant+Garamond:ital,wght@0,400;0,500;0,600;1,400&display=swap">
<style>
  :root {
    --teal-light: #7aa79f;
    --teal: #5b8f86;
    --teal-deep: #3f6b63;
    --teal-ink: #2f554e;
    --paper: #f2f3f2;
    --paper-shade: #e3e6e4;
    --berry: #9b3a5a;
    --backdrop: #d9d6d0;
    --white: #ffffff;
  }
  * { box-sizing: border-box; margin: 0; padding: 0; }
  html, body { width: 1200px; height: 960px; overflow: hidden; }
  body {
    background: var(--backdrop);
    font-family: "Cormorant Garamond", Georgia, serif;
    position: relative;
  }
  .card {
    position: absolute;
    width: 735px;
    height: 420px;
    left: 232px;
    overflow: hidden;
    box-shadow: 0 14px 30px rgba(0,0,0,.22);
  }
  .card--back { top: 40px; background: radial-gradient(circle at 20% 25%, var(--teal-light), var(--teal) 45%, var(--teal-deep) 100%); }
  .card--front { top: 500px; background: var(--paper); }

  /* back */
  .back-floral {
    position: absolute; left: 0; top: 0; width: 300px; height: 300px;
    border-radius: 0 0 300px 0;
    background: radial-gradient(circle at 35% 35%, #86b2aa, #6e9e95 70%);
    opacity: .75;
  }
  .back-name {
    position: absolute; right: 60px; bottom: 96px;
    font-size: 58px; font-weight: 500; color: var(--teal-ink);
    letter-spacing: 1px;
  }
  .back-tagline {
    position: absolute; right: 62px; bottom: 70px;
    font-size: 13px; letter-spacing: 5px; text-transform: uppercase; color: var(--teal-ink);
  }

  /* front */
  .front-art { position: absolute; inset: 0; }
  .identity { position: absolute; left: 120px; top: 62px; color: var(--white); }
  .identity__name { font-size: 30px; font-weight: 600; letter-spacing: 3px; text-transform: uppercase; }
  .identity__title { font-size: 20px; font-style: italic; margin-top: 2px; }
  .contact { list-style: none; position: absolute; left: 92px; top: 170px; color: var(--white); font-size: 19px; }
  .contact li { display: flex; align-items: center; gap: 12px; height: 30px; }
  .contact svg { width: 18px; height: 18px; flex: none; }
  .brand { position: absolute; left: 505px; top: 235px; width: 210px; color: var(--teal-deep); }
  .brand__row { display: flex; align-items: center; gap: 10px; }
  .brand__name { font-size: 34px; font-weight: 500; white-space: nowrap; }
  .brand__dot { width: 12px; height: 12px; border-radius: 50%; background: var(--teal); flex: none; }
  .brand__tag { font-size: 11px; letter-spacing: 3px; text-transform: uppercase; margin-top: 6px; padding-left: 18px; white-space: nowrap; }
</style>
</head>
<body>

<section class="card card--back" aria-label="Card back">
  <div class="back-floral" role="img" aria-label="Faint embossed floral line illustration"></div>
  <div class="back-name">Marren Ashby</div>
  <div class="back-tagline">Truly Yours</div>
</section>

<section class="card card--front" aria-label="Card front">
  <svg class="front-art" viewBox="0 0 735 420" preserveAspectRatio="none" aria-hidden="true">
    <defs>
      <radialGradient id="tealGlow" cx="0.55" cy="0.2" r="0.9">
        <stop offset="0" stop-color="#7aa79f"/>
        <stop offset="0.5" stop-color="#5b8f86"/>
        <stop offset="1" stop-color="#3f6b63"/>
      </radialGradient>
    </defs>
    <polygon points="0,0 440,0 505,420 0,420" fill="url(#tealGlow)"/>
    <polygon points="0,348 10,338 310,338 320,420 0,420" fill="#f2f3f2"/>
    <line x1="40" y1="398" x2="300" y2="398" stroke="#9b3a5a" stroke-width="2"/>
    <polygon points="455,0 463,0 480,238 472,238" fill="#5b8f86"/>
    <polygon points="500,385 505,420 735,420 735,412" fill="#3f6b63"/>
    <polygon points="500,385 735,412 735,420" fill="#5b8f86"/>
  </svg>

  <div class="identity">
    <div class="identity__name">Marren Ashby</div>
    <div class="identity__title">Events Designer</div>
  </div>

  <ul class="contact">
    <li><svg viewBox="0 0 18 18"><rect x="5" y="1.5" width="8" height="15" rx="1.5" fill="none" stroke="#fff" stroke-width="1.5"/></svg>555-214-0187</li>
    <li><svg viewBox="0 0 18 18"><rect x="1.5" y="3.5" width="15" height="11" fill="none" stroke="#fff" stroke-width="1.5"/><path d="M1.5 3.5 9 10 16.5 3.5" fill="none" stroke="#fff" stroke-width="1.5"/></svg>hello@marrenashby.com</li>
    <li><svg viewBox="0 0 18 18"><rect x="2" y="2" width="14" height="14" rx="2" fill="none" stroke="#fff" stroke-width="1.5"/></svg>@marrenashby21</li>
    <li><svg viewBox="0 0 18 18"><circle cx="9" cy="9" r="7" fill="none" stroke="#fff" stroke-width="1.5"/></svg>@trulyyoursdecorating</li>
  </ul>

  <div class="brand">
    <div class="brand__row"><span class="brand__name">Marren Ashby</span><span class="brand__dot"></span></div>
    <div class="brand__tag">Decorating &amp; Florals.</div>
  </div>
</section>

</body>
</html>
```